Simple psychologist website
Open brief, creative designs encouraged
Site map:
Home
our services
our psychologists
selective mutism
resources
contact

Current website:
http://mindsproutyouth.com.au/
Not in love with our logo, or colours etc - open brief
Happy for new font/style/logo for company name - if we choose a logo design from a designer who doesn't win the competition, we will award $50 for the logo and use it in the new website

Website made a few years ago for a sister company that we really like:
http://www.korrelpsychology.com.au/

Clean, credible and warm and friendly look & feel
stock photos OK, designer will be required to hand over any images used in the design as shown in the PSD

Target Market(s)

Adolescents with psychological issues and their families

Industry/Entity Type

Psychology

Number of Pages Required

2 page

Colors

Designer to choose colors to be used in the design.

Requirements
Must have
• One home page - simple with 2 or 3 small areas to tease and attract the user and one template page to suit all the other pages
• We like slides, we want to have 3 slides like korrelpsychology.com.au
• Three slide titles:
• 1. We specialise in many areas, find the right clinical psychologist for your family
• 2. Child Clinical Psychologists in Chatswood and Westmead
• 3. Resources
• Pages structurally similar to
• http://www.korrelpsychology.com.au/
• We like the 'featured' items, which in our case will have splash box titles (can be 3 or 4):
• 1. Selective Mutism
• 2. Is my child anxious?
• 3. Does my child have an eating disorder?
• 4. Parenting adolescents
• Does not need to be a copy of http://www.korrelpsychology.com.au/ and we are willing to accept outside-the-box thinking and design (we in fact encourage it)
• Owner of business wants to highlight Selective Mutism as they have specialists. Consider ways that may make this work.
• Design winner will be based on home page design but winning designer will be required to provide an additional but simpler 'standard' page template design based on the themes used in the winning design.

```html
<!DOCTYPE html>
<html lang="en">
<head>
<meta charset="utf-8">
<title>Mindsprout – Child, Adolescent &amp; Family Psychology</title>
<link rel="stylesheet" href="https://fonts.googleapis.com/css2?family=Didact+Gothic&family=Open+Sans:wght@600;700&display=swap">
<style>
:root{
  --page:#ece7da;
  --blue:#3bb7e0;
  --blue-dark:#1e8fc4;
  --red:#e5466a;
  --pink:#fbe1e4;
  --white:#ffffff;
  --text:#555a5e;
  --green:#2bb673;
  --yellow:#f2c029;
  --magenta:#c23aa9;
}
*{margin:0;padding:0;box-sizing:border-box}
html,body{width:858px;height:1200px;overflow:hidden}
body{background:var(--page);font-family:"Didact Gothic",sans-serif;color:var(--text);position:relative}
a{text-decoration:none}
.abs{position:absolute}
.top-rule{left:0;top:0;width:858px;height:3px;background:var(--red)}
.brand{left:108px;top:26px;display:flex;align-items:center;gap:6px}
.brand-mark{width:12px;height:12px;border-radius:50%;background:var(--blue)}
.brand-name{font-size:20px;color:var(--blue-dark)}
.brand-tag{left:126px;top:52px;font-size:6.5px;color:var(--text)}
.contact{right:108px;top:21px;display:flex;align-items:center;gap:7px;font-size:6.5px;color:var(--blue-dark)}
.contact span{display:flex;align-items:center;gap:4px}
.divider{width:1px;height:16px;background:var(--red)}
.social{right:108px;top:40px;display:flex;gap:6px}
.social i{width:16px;height:16px;border-radius:50%;background:var(--blue-dark);display:block}
.nav{left:0;top:72px;width:858px;height:27px;background:var(--blue)}
.nav ul{list-style:none;position:absolute;left:107px;width:643px;top:0;height:27px;display:flex;justify-content:space-between;align-items:center;font-size:7px;font-family:"Open Sans",sans-serif;font-weight:600;color:var(--white)}
.nav li.active{color:var(--red)}
.nav li.dot{width:3px;height:3px;border-radius:50%;background:var(--red)}
.slider{left:107px;top:110px;width:643px;height:315px;border-radius:8px;overflow:hidden;
  background:
    radial-gradient(ellipse 120px 150px at 190px 130px,#e6c9a6 0%,rgba(230,201,166,0) 100%),
    radial-gradient(ellipse 150px 110px at 180px 240px,#9b2d6e 0%,rgba(155,45,110,0) 100%),
    radial-gradient(ellipse 120px 140px at 480px 140px,#caa184 0%,rgba(202,161,132,0) 100%),
    radial-gradient(ellipse 170px 110px at 500px 260px,#4fb3cf 0%,rgba(79,179,207,0) 100%),
    linear-gradient(90deg,#5a4a44 0%,#8c7a6e 30%,#6a5953 55%,#8a7468 75%,#4d4240 100%)}
.slide-blob{left:309px;top:30px;width:220px;height:108px}
.slide-caption{left:300px;top:56px;width:240px;text-align:center;font-size:16px;line-height:26px;color:var(--white)}
.arrow{width:17px;height:17px;border-radius:50%;border:1.5px solid var(--white);display:flex;align-items:center;justify-content:center}
.tabs{left:73px;top:266px;width:600px;height:50px}
.tab-label{position:absolute;top:24px;font-family:"Open Sans",sans-serif;font-weight:600;font-size:9.5px;color:var(--white)}
.dots{left:10px;top:296px;display:flex;gap:2px}
.dots i{width:7px;height:7px;border:1px solid var(--white);border-radius:2px;display:block}
.card{background:var(--white);border-radius:10px}
.about{left:107px;top:436px;width:643px;height:192px}
.about-photo{left:16px;top:15px;width:209px;height:161px;border-radius:3px;
  background:
    radial-gradient(ellipse 40px 60px at 70px 85px,#c8b8a6 0%,rgba(200,184,166,0) 100%),
    radial-gradient(ellipse 35px 50px at 170px 105px,#8aa3bd 0%,rgba(138,163,189,0) 100%),
    radial-gradient(ellipse 70px 25px at 150px 150px,#6e6e78 0%,rgba(110,110,120,0) 100%),
    linear-gradient(180deg,#dcdad6 0%,#cfcac8 60%,#8f8c92 100%)}
.about-photo span{position:absolute;left:0;top:117px;width:209px;text-align:center;font-size:7px;color:var(--red);font-family:"Open Sans",sans-serif;font-weight:600}
.about h2{position:absolute;left:242px;top:16px;font-weight:400;font-size:16px;color:var(--blue)}
.about .intro{position:absolute;left:242px;top:38px;width:375px;font-size:6.8px;line-height:16px}
.about ul{position:absolute;left:242px;top:82px;list-style:none;font-size:6.8px;line-height:16px}
.about li{display:flex;align-items:center;gap:5px}
.about li svg{flex:none}
.btn{position:absolute;height:20px;border-radius:10px;color:var(--white);font-size:9px;display:flex;align-items:center;justify-content:center}
.btn-blue{background:var(--blue)}
.btn-red{background:var(--red)}
.featured{left:107px;top:640px;width:643px;height:375px}
.feature{background:var(--pink);border-radius:6px;overflow:hidden}
.feature-main{left:11px;top:11px;width:375px;height:353px}
.feature-side{width:236px;height:171px;left:396px}
.feature-title{position:absolute;font-weight:400;font-size:12px;color:var(--red)}
.feature-side .feature-title{font-size:8px;color:var(--blue-dark)}
.feature-text{position:absolute;font-size:6px;line-height:13px;color:#444}
.feature-main .feature-text{font-size:7.3px;line-height:19px}
.footer{left:0;top:1025px;width:858px;height:175px;background:var(--blue);border-top:3px solid var(--red);color:var(--white)}
.footer h3{position:absolute;font-weight:400;font-size:12.5px}
.addr{position:absolute;left:107px;display:flex;font-size:7px;line-height:17px}
.addr b{font-weight:400;font-size:10px;width:56px;display:flex;gap:2px;align-items:flex-start;line-height:14px}
.links{left:395px;top:52px;list-style:none;font-size:7px;line-height:15px;width:95px}
.field{position:absolute;background:#6fcff0;border-radius:2px;font-size:5px;color:#d6f2fb;padding:4px 5px}
.foot-rule{left:103px;top:150px;width:652px;height:1px;background:#6fcff0}
.copyright{left:0;top:157px;width:858px;text-align:center;font-size:6.5px}
.copyright em{font-style:normal;color:var(--red)}
</style>
</head>
<body>
<div class="abs top-rule"></div>

<header>
  <div class="abs brand"><span class="brand-mark"></span><span class="brand-name">Mindsprout</span></div>
  <div class="abs brand-tag">Child, Adolescent &amp; Family Psychology</div>
  <div class="abs contact">
    <span>
      <svg width="13" height="13" viewBox="0 0 14 14"><circle cx="7" cy="7" r="6.3" fill="none" stroke="#1e8fc4"/><path d="M5 4l1.3 1.6-.7.9c.4.9 1 1.5 1.9 1.9l.9-.7L10 9l-.8 1C6.6 9.8 4.2 7.4 4 4.8z" fill="#1e8fc4"/></svg>
      0400 555 218
    </span>
    <i class="divider"></i>
    <span>
      <svg width="14" height="10" viewBox="0 0 14 10"><rect x=".5" y=".5" width="13" height="9" fill="none" stroke="#1e8fc4"/><path d="M.5 .5L7 6l6.5-5.5" fill="none" stroke="#1e8fc4"/></svg>
      info@mindsproutyouth.com.au
    </span>
  </div>
  <div class="abs social"><i></i><i></i><i></i><i></i><i></i></div>
</header>

<nav class="abs nav">
  <ul>
    <li class="active">Home</li><li class="dot"></li>
    <li>Our Services</li><li class="dot"></li>
    <li>Our Psychologists</li><li class="dot"></li>
    <li>Selective Mutism</li><li class="dot"></li>
    <li>Resources</li><li class="dot"></li>
    <li>Contact</li>
  </ul>
</nav>

<section class="abs slider" role="img" aria-label="Photo of an older psychologist talking with a smiling teenage girl in a blue top">
  <svg class="abs slide-blob" viewBox="0 0 220 108" aria-hidden="true">
    <path d="M40 8C80-6 170-4 200 24c26 26 16 68-20 78-40 12-120 10-150-8C0 78 6 24 40 8z" fill="#3bb7e0" opacity=".8"/>
  </svg>
  <p class="abs slide-caption">We specialise in many<br>areas, find the right clinical<br>psychologist for your<br>family!</p>
  <div class="abs arrow" style="left:15px;top:189px"><svg width="7" height="7" viewBox="0 0 7 7"><path d="M5 .5L2 3.5 5 6.5" fill="none" stroke="#fff" stroke-width="1.4"/></svg></div>
  <div class="abs arrow" style="left:611px;top:189px"><svg width="7" height="7" viewBox="0 0 7 7"><path d="M2 .5L5 3.5 2 6.5" fill="none" stroke="#fff" stroke-width="1.4"/></svg></div>
  <svg class="abs tabs" viewBox="0 0 600 50" aria-hidden="true">
    <path d="M0 10Q0 0 12 0Q90 6 170 0L172 50H0z" fill="#2bb673" opacity=".9"/>
    <path d="M170 0Q250 8 332 2L332 50H172z" fill="#f2c029" opacity=".9"/>
    <path d="M332 2Q420 10 498 0Q504 25 498 50H332z" fill="#c23aa9" opacity=".9"/>
  </svg>
  <div class="abs" style="left:73px;top:266px;width:600px;height:50px">
    <span class="tab-label" style="left:50px">DEPRESSION</span>
    <span class="tab-label" style="left:203px">FEARS AND ANXIETY</span>
    <span class="tab-label" style="left:345px">PARENT-CHILD RELATIONSHIPS</span>
  </div>
  <div class="abs dots"><i></i><i></i><i></i></div>
</section>

<section class="abs card about">
  <div class="abs about-photo" role="img" aria-label="Photo of a psychologist with a young boy in a bright playroom"><span>GET TO KNOW OUR PSYCHOLOGISTS</span></div>
  <h2>About Us</h2>
  <p class="intro">We are a group of clinical psychologists at Chatswood and Westmead (Sydney). We provide a range of services including the following:</p>
  <ul>
    <li><svg width="10" height="10" viewBox="0 0 10 10"><circle cx="5" cy="5" r="4" fill="none" stroke="#e5466a"/><path d="M3 5l1.5 1.5L7 3.5" fill="none" stroke="#e5466a"/></svg>Individual counselling and therapy for kids, teens and families</li>
    <li><svg width="10" height="10" viewBox="0 0 10 10"><circle cx="5" cy="5" r="4" fill="none" stroke="#e5466a"/><path d="M3 5l1.5 1.5L7 3.5" fill="none" stroke="#e5466a"/></svg>Family consultations</li>
    <li><svg width="10" height="10" viewBox="0 0 10 10"><circle cx="5" cy="5" r="4" fill="none" stroke="#e5466a"/><path d="M3 5l1.5 1.5L7 3.5" fill="none" stroke="#e5466a"/></svg>Seminars and training with schools</li>
    <li><svg width="10" height="10" viewBox="0 0 10 10"><circle cx="5" cy="5" r="4" fill="none" stroke="#e5466a"/><path d="M3 5l1.5 1.5L7 3.5" fill="none" stroke="#e5466a"/></svg>Brief group programmes for anxiety, stress and body image concerns for adolescents</li>
  </ul>
  <a class="btn btn-blue" style="left:254px;top:156px;width:80px">Read more</a>
</section>

<section class="abs card featured">
  <article class="abs feature feature-main">
    <div class="abs" style="left:0;top:0;width:375px;height:192px;background:
      radial-gradient(ellipse 90px 110px at 90px 110px,#c77a4e 0%,rgba(199,122,78,0) 100%),
      radial-gradient(ellipse 80px 100px at 290px 120px,#5f8fc0 0%,rgba(95,143,192,0) 100%),
      radial-gradient(ellipse 50px 40px at 270px 50px,#d7a27f 0%,rgba(215,162,127,0) 100%),
      radial-gradient(ellipse 60px 30px at 200px 170px,#e2574c 0%,rgba(226,87,76,0) 100%),
      linear-gradient(90deg,#eeeae5 0%,#e4ddd4 50%,#f0ede9 100%)" role="img" aria-label="Photo of a psychologist sitting with a thoughtful red-haired boy"></div>
    <svg class="abs" style="left:0;top:170px" width="375" height="40" viewBox="0 0 375 40" aria-hidden="true">
      <path d="M0 22Q90 0 190 26T375 14V40H0z" fill="#fbe1e4"/>
      <path d="M0 22Q90 0 190 26T375 14" fill="none" stroke="#e5466a" stroke-width="2.5"/>
    </svg>
    <h3 class="feature-title" style="left:11px;top:214px">SELECTIVE MUTISM IN CHILD</h3>
    <p class="feature-text" style="left:11px;top:236px;width:340px">Elena Voss, Clinical Psychologist at Mindsprout has many years of working with children with selective mutism. She is currently also undertaking research in this area of child anxiety. She has been asked to present to school counsellors, teachers and parents. Please click on the following link to access her most recent presentation........</p>
    <a class="btn btn-red" style="left:11px;top:321px;width:81px">Read more</a>
  </article>

  <article class="abs feature feature-side" style="top:11px">
    <div class="abs" style="left:0;top:0;width:236px;height:110px;background:
      radial-gradient(ellipse 45px 55px at 110px 55px,#8a7a70 0%,rgba(138,122,112,0) 100%),
      radial-gradient(ellipse 80px 25px at 110px 95px,#2c2a2b 0%,rgba(44,42,43,0) 100%),
      linear-gradient(90deg,#3e3a38 0%,#5d5550 50%,#6e5e50 100%)" role="img" aria-label="Photo of a tired teenager sitting on a couch"></div>
    <svg class="abs" style="left:0;top:100px" width="236" height="16" viewBox="0 0 236 16" aria-hidden="true"><path d="M0 8Q60 -2 120 8T236 6V16H0z" fill="#fbe1e4"/><path d="M0 8Q60 -2 120 8T236 6" fill="none" stroke="#3bb7e0" stroke-width="2"/></svg>
    <h3 class="feature-title" style="left:11px;top:120px">HELPING YOUR ADOLESCENT SLEEP BETTER</h3>
    <p class="feature-text" style="left:11px;top:132px;width:218px">The way we think about sleep (and not sleeping) has a big impact on us. In particular, if your child ...</p>
    <a class="btn btn-blue" style="left:172px;top:151px;width:54px;height:14px;font-size:6.5px">Read more</a>
  </article>

  <article class="abs feature feature-side" style="top:193px">
    <div class="abs" style="left:0;top:0;width:236px;height:110px;background:
      radial-gradient(ellipse 50px 60px at 60px 60px,#8f7f6c 0%,rgba(143,127,108,0) 100%),
      radial-gradient(ellipse 40px 50px at 195px 75px,#8ec3de 0%,rgba(142,195,222,0) 100%),
      radial-gradient(ellipse 35px 25px at 150px 45px,#e6a04a 0%,rgba(230,160,74,0) 100%),
      linear-gradient(90deg,#5e5650 0%,#a79c90 50%,#e7e4df 100%)" role="img" aria-label="Photo of a woman taking notes beside a young boy drawing"></div>
    <svg class="abs" style="left:0;top:100px" width="236" height="16" viewBox="0 0 236 16" aria-hidden="true"><path d="M0 8Q60 -2 120 8T236 6V16H0z" fill="#fbe1e4"/><path d="M0 8Q60 -2 120 8T236 6" fill="none" stroke="#3bb7e0" stroke-width="2"/></svg>
    <h3 class="feature-title" style="left:11px;top:120px">WHY IS MY CHILD ANXIOUS?</h3>
    <p class="feature-text" style="left:11px;top:132px;width:218px">Understanding childhood anxiety Anxiety is a normal and sometimes helpful emotion in all children. Some children......</p>
    <a class="btn btn-blue" style="left:172px;top:151px;width:54px;height:14px;font-size:6.5px">Read more</a>
  </article>
</section>

<footer class="abs footer">
  <h3 style="left:107px;top:28px">ADDRESS</h3>
  <div class="addr" style="top:52px">
    <b><svg width="9" height="12" viewBox="0 0 9 12"><path d="M4.5 11.5S.5 7 .5 4.5a4 4 0 018 0C8.5 7 4.5 11.5 4.5 11.5z" fill="none" stroke="#e5466a"/><circle cx="4.5" cy="4.5" r="1.3" fill="#e5466a"/></svg>Westmead</b>
    <span style="margin-left:12px">Suite 12, level 2, Parkside Health Rooms<br>48 Banksia Lane, Westmead NSW 2145</span>
  </div>
  <div class="addr" style="top:92px">
    <b><svg width="9" height="12" viewBox="0 0 9 12"><path d="M4.5 11.5S.5 7 .5 4.5a4 4 0 018 0C8.5 7 4.5 11.5 4.5 11.5z" fill="none" stroke="#e5466a"/><circle cx="4.5" cy="4.5" r="1.3" fill="#e5466a"/></svg>Chatswood</b>
    <span style="margin-left:12px">Suite 7A, 22 Wattle Street<br>Chatswood NSW 2067</span>
  </div>

  <h3 style="left:394px;top:28px">QUICK LINKS</h3>
  <ul class="abs links">
    <li>Areas of specialty</li>
    <li>Making an appointment</li>
    <li>Who can refer</li>
    <li>What to expect at the first appointment</li>
  </ul>

  <h3 style="left:563px;top:28px">We Love To Hear From You!</h3>
  <div class="field" style="left:563px;top:55px;width:91px;height:15px">Full Name</div>
  <div class="field" style="left:659px;top:55px;width:91px;height:15px">Email Address</div>
  <div class="field" style="left:563px;top:75px;width:187px;height:29px">Message</div>
  <a class="btn btn-red" style="left:563px;top:113px;width:53px;height:14px;font-size:7px">Send</a>

  <div class="abs foot-rule"></div>
  <p class="abs copyright">Copyright @ <em>Mindsprout</em>. All rights reserved.</p>
</footer>
</body>
</html>
```